Simple Modern Label for a Coconut oil product

We need a label designed for Organic Coconut oil. We would like the label to convey the gourmet/high quality product. It should be modern and simple and look like an artisinal product. The label will need to contain all the basic label requirements - Independence list, place for nutrition facts, our company logo etc.
The label will ultimately be printed as oil proof, so it will have a glossy appearance.
I have includes some examples that I like and a file with the logo.

Product Container - Wide Mount Clear Glass Jar: 4.75 inches tall (base to the bottom of the lid) and 9.5 in circumference
Label: Can be 1 or 2 separate labels, round, square and rectangle are okay
No larger than 3 inches high and 9 inches long

Target Market(s)

Middle Age home chef

Industry/Entity Type

Product

Requirements
Must have
• - logo (Attached below, I have this in multiple formats, let me know if you need them)
• - 14 FL OZ (414mL)
• - ingredient: organic unrefined whole kernel virgin coconut oil,
• - Manufacturer: XXX Y St., anywhere, CA, 99999
• - Distributed by Fernvale Naturals, P.O. Box 5521, Oakland, CA 94610 www.FernvaleNaturals.example
• - Certified Organic by Company Name
• - Product of Sri Lanka
Nice to have
• - Nutrition Facts
Should not have
• Clutter

```html
<!DOCTYPE html>
<html lang="en">
<head>
<meta charset="UTF-8">
<title>Fernvale Naturals Coconut Oil Label</title>
<link href="https://fonts.googleapis.com/css2?family=Quicksand:wght@300;500&family=Kaushan+Script&family=Jost:wght@500&display=swap" rel="stylesheet">
<style>
  :root {
    --paper: #ffffff;
    --cocoa: #5a1e0f;
    --sky: #3f8fd2;
    --lagoon: #72cdd6;
    --aqua: #58c6e6;
    --navy: #12386b;
  }
  * { margin: 0; padding: 0; box-sizing: border-box; }
  html, body { width: 1037px; height: 1200px; overflow: hidden; background: var(--paper); }
  .label {
    position: relative;
    width: 1037px;
    height: 1200px;
    background: var(--paper);
    display: flex;
    flex-direction: column;
    align-items: center;
  }
  .brand {
    margin-top: 170px;
    display: flex;
    align-items: center;
    gap: 14px;
    font-family: 'Quicksand', sans-serif;
    font-weight: 500;
    font-size: 26px;
    color: var(--navy);
  }
  .brand-mark {
    width: 26px;
    height: 26px;
    background: var(--navy);
  }
  .coconut-band {
    margin-top: 90px;
    width: 720px;
    height: 130px;
  }
  .tagline {
    font-family: 'Quicksand', sans-serif;
    font-weight: 300;
    line-height: 1;
    text-align: center;
    white-space: nowrap;
  }
  .tagline-quality {
    margin-top: 28px;
    font-size: 56px;
    letter-spacing: 10px;
    color: var(--sky);
  }
  .tagline-grade {
    margin-top: 6px;
    font-size: 56px;
    letter-spacing: 27px;
    color: var(--lagoon);
  }
  .product-name {
    position: relative;
    width: 720px;
    height: 280px;
    font-family: 'Kaushan Script', cursive;
    text-align: center;
  }
  .product-name .word-main {
    position: absolute;
    left: 0; right: 0; top: 0;
    font-size: 170px;
    line-height: 1;
    color: var(--sky);
  }
  .product-name .word-sub {
    position: absolute;
    left: 0; right: 60px; top: 118px;
    font-size: 150px;
    line-height: 1;
    color: var(--aqua);
  }
  .volume {
    margin-top: 20px;
    font-family: 'Jost', sans-serif;
    font-weight: 500;
    font-size: 30px;
    letter-spacing: 1px;
    color: var(--cocoa);
  }
</style>
</head>
<body>
  <main class="label">
    <div class="brand">
      <span class="brand-mark"></span>
      <span class="brand-name">Fernvale Naturals</span>
    </div>

    <svg class="coconut-band" viewBox="0 0 720 130" role="img" aria-label="Row of stylised brown coconut halves with white flesh and dripping milk">
      <rect width="720" height="130" fill="var(--cocoa)"/>
    </svg>

    <p class="tagline tagline-quality">premium organic</p>
    <p class="tagline tagline-grade">extra virgin</p>

    <h1 class="product-name">
      <span class="word-main">Coconut</span>
      <span class="word-sub">Oil</span>
    </h1>

    <p class="volume">14 FL OZ (414mL)</p>
  </main>
</body>
</html>
```